Zielgruppe
Wir sind eine Imkerei mit angeschlossenem Lehrgarten. Unsere Produktpalette umfasst selbst hergestellte Imkereiprodukte aller Art (Honig, Bienenwachskerzen, Propolis, Pollen, Met). Unsere Zielgruppe sind solvente, umweltbewusste Konsumenten mit dem Sinn für nachhaltig und regional produzierte Waren.
Aufgabenstellung
- Das Etikett soll maximal die Logo-Farben nutzen (weiß, schwarz, gelb), evtl. mit goldenen Akzenten.
- Logo 'Imkerei Fam. Halvers' integrieren
- Ein gleich aussehendes Grundetikett für mehrere Sorten
- Honigname 'Dünenglanz' + Sortenbezeichnung (Rapshonig, Frühtrachthonig, Sommertrachthonig), zusätzlich ein 'Leeretikett' zum Einstempeln von Sondersorten
- Optische Elemente gerne Waben und/oder Regionales (Friesland, Jadebusen, Nordsee)
- Wir erweitern Stück für Stück unser Sortiment, daher soll das Grunddesign später auf Etiketten für zum Beispiel Met, Seife und Bonbons auszuweiten sein.
- Etiketten in 3 verschiedenen Größen nutzbar (500g, 250g, 50g)
- Pflichtangaben auf Honigetiketten: Deutscher Honig/ Honig aus Deutschland, Füllmenge (Schriftgröße mind. 4 mm Höhe), Hersteller/ Name und Anschrift des Imkers (zunächst Platzhalter nutzen, Daten werden im Verlauf übermittelt), Platz für Datumsstempel (MHD), Lagerbedingung (kühl, trocken und dunkel lagern)
- Das Etikett soll einen Gewährverschluss haben, obenauf das leere Feld für den Datumsstempel
- Das Honigglas hat einen goldenen Deep Twist Off Deckel

```html
<!DOCTYPE html>
<html lang="de">
<head>
<meta charset="utf-8">
<title>Dünenglanz – Honigetikett 250 g</title>
<link href="https://fonts.googleapis.com/css2?family=Amatic+SC:wght@400;700&family=Norican&display=swap" rel="stylesheet">
<style>
  :root {
    --paper: #f1ece0;
    --ink: #262624;
    --outline: #555555;
    --honey: #f4c43a;
    --honey-text: #f0b91a;
    --gold: #c2951c;
  }
  html, body {
    margin: 0;
    padding: 0;
    width: 955px;
    height: 1200px;
    overflow: hidden;
    background: var(--paper);
  }
  .label {
    position: relative;
    width: 955px;
    height: 1200px;
    background: var(--paper);
    font-family: "Amatic SC", sans-serif;
    color: var(--ink);
  }
  .label__shapes {
    position: absolute;
    inset: 0;
  }
  .best-before {
    position: absolute;
    left: 374px;
    top: 66px;
    width: 200px;
    margin: 0;
    text-align: center;
    font-size: 33px;
    font-weight: 700;
    line-height: 1.05;
    letter-spacing: 0.5px;
  }
  .vertical {
    position: absolute;
    white-space: nowrap;
    transform-origin: left top;
    transform: rotate(-90deg);
    margin: 0;
    font-weight: 700;
    letter-spacing: 0.5px;
  }
  .producer-name {
    left: 430px;
    top: 686px;
    font-size: 28px;
    color: var(--honey-text);
  }
  .producer-address {
    left: 484px;
    top: 726px;
    font-size: 30px;
  }
  .storage {
    left: 46px;
    top: 1134px;
    font-size: 30px;
  }
  .origin {
    position: absolute;
    left: 364px;
    top: 786px;
    width: 300px;
    margin: 0;
    text-align: center;
    font-size: 46px;
    font-weight: 700;
    letter-spacing: 0.5px;
  }
  .honey-name {
    position: absolute;
    left: 240px;
    top: 815px;
    width: 480px;
    margin: 0;
    text-align: center;
    font-family: "Norican", cursive;
    font-weight: 400;
    font-size: 92px;
    line-height: 1.1;
  }
  .net-weight {
    position: absolute;
    left: 818px;
    top: 820px;
    margin: 0;
    font-size: 38px;
    font-weight: 700;
    transform: rotate(14deg);
  }
  .brand {
    position: absolute;
    left: 706px;
    top: 1012px;
    width: 190px;
    margin: 0;
    text-align: center;
    font-size: 34px;
    font-weight: 700;
    line-height: 1;
    color: var(--gold);
  }
</style>
</head>
<body>
<main class="label">
  <svg class="label__shapes" width="955" height="1200" viewBox="0 0 955 1200">
    <path class="label__cut-outline" d="M384,743 V357 L291,191 L384,26 H571 L664,191 L571,357 V743 H939 V1185 H17 V743 Z"
          fill="none" stroke="var(--outline)" stroke-width="2.5"/>
    <g class="honeycomb" fill="var(--honey)">
      <polygon points="287,774 382,830 382,940 287,996 192,940 192,830"/>
      <polygon points="477,774 572,830 572,940 477,996 382,940 382,830"/>
      <polygon points="668,774 763,830 763,940 668,996 573,940 573,830"/>
    </g>
    <path class="trail" d="M238,1137 C420,1125 640,1140 800,1130 C880,1125 910,1060 880,1000 C850,955 720,950 660,975 C620,995 640,1040 700,1015 C730,1000 732,960 735,940 L735,880 Q740,850 790,836"
          fill="none" stroke="var(--ink)" stroke-width="4" stroke-dasharray="14 10" stroke-linecap="round"/>
    <rect class="lighthouse" x="121" y="795" width="117" height="346" fill="var(--ink)"
          role="img" aria-label="Illustration eines schwarz-weiß gestreiften Leuchtturms"/>
  </svg>

  <p class="best-before">Mindestens<br>haltbar bis:</p>

  <p class="vertical producer-name">Imkerei Familie Halvers GmbH</p>
  <p class="vertical producer-address">Musterstr. 1, 12345 Musterhausen</p>
  <p class="vertical storage">Kühl, trocken und dunkel lagern</p>

  <p class="origin">Deutscher Honig</p>
  <h1 class="honey-name">Dünenglanz</h1>
  <p class="net-weight">250 g</p>

  <p class="brand">Fam. Halvers<br>Imkerei</p>
</main>
</body>
</html>
```